Webpage for a treatment housing for young addicts.

I need a new design and files for my wordpress page. I need it to be more neat and clean. I need it to look professional with a starting page that will work as a navigation. I need like logo and phone number and such up top, a picture under it with one sentence as a slogan and under it 6 boxes to click to come to our different pages. Under it I want news etc.

Target Market(s)

Social services, employees and governements

Coding

Coded - Design and coding required

Font styles to use
Sans Serif

Colors
abd037
3176b5
9d9d9d
aaaaaa
f04a50

Requirements
Must have
• A nice design
Nice to have
• need it to look professional with a starting page that will work as a navigation. I need like logo and phone number and such up top, a picture under it with one sentence as a slogan and under it 6 boxes to click to come to our different pages. Under it I want news etc.
• today www.kolrev.se
• want more like www.tralvik.se or www.bersona.se
Should not have
• To many different colours and a messy design.

```html
<!DOCTYPE html>
<html lang="sv">
<head>
<meta charset="utf-8">
<title>Kolrev – Omsorg Vård Boende</title>
<link href="https://fonts.googleapis.com/css2?family=Poppins:wght@300;400;500;600;700&display=swap" rel="stylesheet">
<style>
:root{
  --blue:#0d55a8;
  --blue-dark:#0a4b97;
  --green:#8cc63f;
  --green-dark:#20a84f;
  --grey-bg:#f1f2f5;
  --mint-bg:#e5f3f5;
  --text:#3c3c3c;
  --muted:#6b6b6b;
  --white:#fff;
}
*{margin:0;padding:0;box-sizing:border-box}
html,body{width:1200px;height:2788px;overflow:hidden}
body{position:relative;font-family:"Poppins",sans-serif;color:var(--text);background:var(--white)}
.abs{position:absolute}
a{color:inherit;text-decoration:none}

.topbar{left:0;top:0;width:1200px;height:27px;background:var(--blue)}
.topbar a{position:absolute;top:6px;font-size:12px;color:var(--white)}

.header{left:0;top:27px;width:1200px;height:76px;background:var(--white);border-bottom:1px solid #e4e4e4}
.brand{left:128px;top:14px;display:flex;align-items:center;gap:10px}
.brand-mark{width:34px;height:34px;border-radius:50%;background:var(--green)}
.brand-name{font-size:30px;font-weight:700;color:var(--blue);line-height:1}
.brand-sub{font-size:8px;color:var(--muted);letter-spacing:1px;margin-top:2px}
.hcell{top:0;height:76px;border-left:1px solid #e4e4e4;display:flex;align-items:center}
.hcell .big{font-size:19px;color:#333;line-height:1.1}
.hcell .small{font-size:12px;color:#555}
.hcell svg{margin-right:8px}

.hero{left:0;top:103px;width:1200px;height:382px;background:radial-gradient(ellipse at 60% 50%,#8a6a4c 0%,#4f5a3a 45%,#2d3a28 100%)}
.hero h1{position:absolute;left:118px;top:150px;font-size:42px;font-weight:700;color:var(--white);line-height:50px}
.hero h1 span{color:var(--green)}
.arrow-btn{width:38px;height:38px;border-radius:50%;background:var(--green);top:280px;display:flex;align-items:center;justify-content:center}

.tiles{left:0;top:485px;width:1200px;height:183px;background:var(--grey-bg)}
.tile{position:absolute;width:307px;height:51px;background:var(--white);display:flex;align-items:center;justify-content:space-between;padding:0 22px;font-size:17px;color:#444}

.news{left:0;top:668px;width:1200px;height:490px;background:#f3f4f6}
.sec-title{position:absolute;left:0;width:1200px;text-align:center;font-size:28px;color:#444}
.rule{position:absolute;left:582px;width:36px;height:2px;background:var(--green)}
.news .sec-title{color:var(--blue);font-size:31px}
.news .rule{background:var(--blue)}
.lead{position:absolute;left:370px;top:114px;width:460px;text-align:center;font-size:12px;line-height:21px;color:#666}
.news-item{position:absolute;width:313px;height:79px;background:var(--white);padding:15px 22px}
.news-item time{display:block;font-size:10px;color:#555}
.news-item p{font-size:15px;line-height:19px;color:#444}
.btn{position:absolute;display:flex;align-items:center;justify-content:center;gap:8px;background:var(--green);color:var(--white);font-size:12px}

.jobs{left:0;top:1158px;width:1200px;height:120px;background:var(--blue)}
.jobs h2{position:absolute;left:331px;top:40px;font-size:26px;font-weight:500;color:var(--white)}

.photo{position:absolute}
.card-cap{position:absolute;width:260px;text-align:center;font-size:17px;color:#555}
.card-link{position:absolute;width:260px;text-align:center;font-size:15px;color:var(--blue)}

.more{left:0;top:1800px;width:1200px;height:345px;background:var(--grey-bg)}
.info-card{position:absolute;width:320px;height:205px;background:var(--white)}
.info-card .cap{position:absolute;left:11px;top:167px;font-size:15px;color:#444;display:flex;align-items:center;gap:10px}

.newsletter{left:0;top:2145px;width:1200px;height:212px;background:var(--mint-bg)}
.nl-input{position:absolute;left:303px;top:120px;width:425px;height:42px;background:var(--white);border:1px solid #d4d4d4;font-size:12px;color:#888;padding:12px 20px}
.nl-btn{position:absolute;left:728px;top:120px;width:169px;height:42px;background:var(--green-dark);color:var(--white);font-size:13px;display:flex;align-items:center;justify-content:center}

.footer{left:0;top:2357px;width:1200px;height:431px;background:var(--blue);color:var(--white)}
.fcol-title{position:absolute;top:63px;font-size:13px;font-weight:500}
.fcol-title::after{content:"";position:absolute;left:0;top:25px;width:37px;height:2px;background:var(--white)}
.flink{position:absolute;left:156px;font-size:15px}
.contact{position:absolute;left:409px;display:flex;gap:22px}
.contact .big{font-size:20px;line-height:24px}
.contact .small{font-size:15px;line-height:22px}
.social{position:absolute;left:916px;display:flex;align-items:center;gap:17px;font-size:15px}
.social i{display:block;width:24px;height:24px;border:2px solid var(--white);border-radius:3px}
.copy{position:absolute;left:0;top:350px;width:1200px;border-top:1px solid rgba(255,255,255,.25);padding-top:28px;text-align:center;font-size:15px}
.vline{position:absolute;top:0;width:1px;height:351px;background:rgba(255,255,255,.25)}
</style>
</head>
<body>

<nav class="abs topbar">
  <a style="left:805px" href="#">Länk</a>
  <a style="left:879px" href="#">Länk</a>
  <a style="left:953px" href="#">Länk</a>
  <a style="left:1027px" href="#">Länk</a>
</nav>

<header class="abs header">
  <div class="abs brand">
    <span class="brand-mark"></span>
    <div>
      <div class="brand-name">Kolrev</div>
      <div class="brand-sub">Omsorg Vård Boende</div>
    </div>
  </div>
  <div class="abs hcell" style="left:430px;width:265px;padding-left:18px">
    <svg width="28" height="28" viewBox="0 0 24 24" fill="none" stroke="#0d55a8" stroke-width="1.6"><path d="M5 3h4l2 5-2.5 1.5a11 11 0 0 0 6 6L16 13l5 2v4a2 2 0 0 1-2 2A16 16 0 0 1 3 5a2 2 0 0 1 2-2z"/></svg>
    <div><div class="big">010-4400870</div><div class="small">Växeln är öppen vardagar 8-17</div></div>
  </div>
  <div class="abs hcell" style="left:695px;width:198px;padding-left:16px">
    <svg width="32" height="26" viewBox="0 0 24 20" fill="none" stroke="#0d55a8" stroke-width="1.4"><path d="M1 9 23 1 17 19l-6-6-3 5v-7L23 1"/></svg>
    <div><div class="big">Kontakta oss</div><div class="small">Fler kontaktuppgifter</div></div>
  </div>
  <div class="abs hcell" style="left:893px;width:65px;flex-direction:column;justify-content:center">
    <svg width="28" height="28" viewBox="0 0 24 24" fill="none" stroke="#333" stroke-width="1.8"><circle cx="10" cy="10" r="7"/><path d="m15 15 7 7"/></svg>
    <span style="font-size:8px;color:#555">SÖK</span>
  </div>
  <div class="abs hcell" style="left:958px;width:117px;border-right:1px solid #e4e4e4;padding-left:20px;font-size:14px;color:#444">
    <svg width="28" height="16" viewBox="0 0 28 16" stroke="#444" stroke-width="1.5"><path d="M0 2h28M0 8h28M0 14h28"/></svg>MENY
  </div>
</header>

<section class="abs hero" role="img" aria-label="Photo of hands planting a small cactus in a terracotta pot">
  <h1>”Vi skapar Hållbara <span>vägar till</span><br>&nbsp;en Bättre framtid”</h1>
  <a class="abs arrow-btn" style="left:29px" href="#"><svg width="10" height="12" viewBox="0 0 10 12" fill="none" stroke="#fff" stroke-width="1.6"><path d="M7 1 2 6l5 5"/></svg></a>
  <a class="abs arrow-btn" style="left:1133px" href="#"><svg width="10" height="12" viewBox="0 0 10 12" fill="none" stroke="#fff" stroke-width="1.6"><path d="M3 1l5 5-5 5"/></svg></a>
</section>

<section class="abs tiles">
  <a class="tile" style="left:125px;top:41px" href="#">HVB <svg width="14" height="12" viewBox="0 0 14 12" fill="none" stroke="#0d55a8" stroke-width="1.6"><path d="m1 1 5 5-5 5M7 1l5 5-5 5"/></svg></a>
  <a class="tile" style="left:447px;top:41px" href="#">Stödboende <svg width="14" height="12" viewBox="0 0 14 12" fill="none" stroke="#0d55a8" stroke-width="1.6"><path d="m1 1 5 5-5 5M7 1l5 5-5 5"/></svg></a>
  <a class="tile" style="left:768px;top:41px" href="#">Öppenvård <svg width="14" height="12" viewBox="0 0 14 12" fill="none" stroke="#0d55a8" stroke-width="1.6"><path d="m1 1 5 5-5 5M7 1l5 5-5 5"/></svg></a>
  <a class="tile" style="left:125px;top:104px" href="#">Vårt arbetssätt <svg width="14" height="12" viewBox="0 0 14 12" fill="none" stroke="#0d55a8" stroke-width="1.6"><path d="m1 1 5 5-5 5M7 1l5 5-5 5"/></svg></a>
  <a class="tile" style="left:447px;top:104px" href="#">Om Oss <svg width="14" height="12" viewBox="0 0 14 12" fill="none" stroke="#0d55a8" stroke-width="1.6"><path d="m1 1 5 5-5 5M7 1l5 5-5 5"/></svg></a>
  <a class="tile" style="left:768px;top:104px" href="#">Sök placerig <svg width="14" height="12" viewBox="0 0 14 12" fill="none" stroke="#0d55a8" stroke-width="1.6"><path d="m1 1 5 5-5 5M7 1l5 5-5 5"/></svg></a>
</section>

<section class="abs news">
  <h2 class="sec-title" style="top:50px">Nyheter</h2>
  <div class="rule" style="top:101px"></div>
  <p class="lead">Lorem ipsum dolor sit amet, consectetur adipisicing elit, sed do eiusmod tempor incididunt ut labore et.</p>
  <article class="news-item" style="left:128px;top:204px"><time>2018-12-20</time><p>Lorem ipsum dolor sit amet, consectetur adipisicing elit, sed</p></article>
  <article class="news-item" style="left:445px;top:204px;padding-left:13px"><time>2018-12-18</time><p>Lorem ipsum dolor sit amet, consectetur adipisicing elit, sed</p></article>
  <article class="news-item" style="left:762px;top:204px"><time>2018-12-17</time><p>Lorem ipsum dolor sit amet,</p></article>
  <article class="news-item" style="left:128px;top:287px"><time>2018-12-14</time><p>Lorem ipsum dolor sit amet, consectetur adipisicing elit, sed</p></article>
  <article class="news-item" style="left:445px;top:287px;padding-left:13px"><time>2018-11-29</time><p>Lorem ipsum dolor sit amet,</p></article>
  <article class="news-item" style="left:762px;top:287px"><time>2018-11-23</time><p>Lorem ipsum dolor sit amet, consectetur adipisicing elit, sed</p></article>
  <a class="btn" style="left:518px;top:393px;width:164px;height:36px" href="#">Nyhetsarkivet <svg width="16" height="10" viewBox="0 0 16 10" fill="none" stroke="#fff" stroke-width="1.4"><path d="M0 5h15M11 1l4 4-4 4"/></svg></a>
</section>

<section class="abs jobs">
  <h2>Lediga Jobb</h2>
  <a class="btn" style="left:751px;top:41px;width:120px;height:37px" href="#">Sök jobb <svg width="18" height="18" viewBox="0 0 24 24" fill="none" stroke="#fff" stroke-width="1.6"><circle cx="10" cy="10" r="7"/><path d="m15 15 7 7"/></svg></a>
</section>

<section>
  <h2 class="sec-title" style="top:1340px">Kolrev på sociala medier</h2>
  <div class="rule" style="top:1386px;background:var(--blue)"></div>
  <div class="photo" style="left:128px;top:1416px;width:252px;height:253px;background:linear-gradient(160deg,#7d6e62,#3d5a4e)" role="img" aria-label="Photo of a smiling man in a green sweater at a desk"></div>
  <div class="photo" style="left:473px;top:1416px;width:253px;height:253px;background:linear-gradient(160deg,#c9ced6,#3a4b72)" role="img" aria-label="Photo of a technician in a cap giving a thumbs up"></div>
  <div class="photo" style="left:822px;top:1416px;width:253px;height:253px;background:linear-gradient(160deg,#cfd2d6,#4d4f55)" role="img" aria-label="Photo of two colleagues reading documents together"></div>
  <p class="card-cap" style="left:131px;top:1677px">Välj bland våra olika sidor</p>
  <p class="card-cap" style="left:476px;top:1679px">Följ oss i vår vardag</p>
  <p class="card-cap" style="left:823px;top:1679px">Vi söker talanger</p>
  <a class="card-link" style="left:114px;top:1723px" href="#">Fotobok ›</a>
  <a class="card-link" style="left:468px;top:1722px" href="#">Bildflöde ›</a>
  <a class="card-link" style="left:818px;top:1723px" href="#">Yrkesnät ›</a>
</section>

<section class="abs more">
  <h2 class="sec-title" style="top:30px">Mer information</h2>
  <div class="rule" style="top:75px;background:var(--blue)"></div>
  <div class="info-card" style="left:268px;top:93px">
    <div style="height:160px;background:linear-gradient(180deg,#e9ebe8,#7a7f86)" role="img" aria-label="Photo of a group of colleagues standing together in an office"></div>
    <p class="cap">We are a member off on one <svg width="16" height="10" viewBox="0 0 16 10" fill="none" stroke="#0d55a8" stroke-width="1.4"><path d="M0 5h15M11 1l4 4-4 4"/></svg></p>
  </div>
  <div class="info-card" style="left:612px;top:93px">
    <div style="height:160px;background:linear-gradient(100deg,#6f7884,#dfe2e5)" role="img" aria-label="Photo of two business people shaking hands"></div>
    <p class="cap">We work with: for the other one <svg width="16" height="10" viewBox="0 0 16 10" fill="none" stroke="#0d55a8" stroke-width="1.4"><path d="M0 5h15M11 1l4 4-4 4"/></svg></p>
  </div>
</section>

<section class="abs newsletter">
  <div class="abs" style="left:135px;top:18px;width:225px;height:194px;background:linear-gradient(160deg,#4fd17a 0%,#f6c451 45%,#f39c24 100%);border-radius:40px 40px 0 0" role="img" aria-label="Illustration of an envelope with a letter and a check mark"></div>
  <h2 class="sec-title" style="top:68px;font-size:20px">Prenumerera på vårt nyhetsbrev</h2>
  <div class="rule" style="top:100px"></div>
  <div class="nl-input">E-post</div>
  <a class="nl-btn" href="#">Subscribe</a>
</section>

<footer class="abs footer">
  <div class="vline" style="left:361px"></div>
  <div class="vline" style="left:862px"></div>

  <h3 class="fcol-title" style="left:156px">MENY</h3>
  <a class="flink" style="top:108px" href="#">Hem</a>
  <a class="flink" style="top:145px" href="#">Om Kolrev</a>
  <a class="flink" style="top:183px" href="#">Linnegården HVB</a>
  <a class="flink" style="top:220px" href="#">Jobba hos oss</a>
  <a class="flink" style="top:258px" href="#">Kontakt</a>
  <a class="flink" style="top:295px" href="#">Blog</a>

  <h3 class="fcol-title" style="left:409px">KONTAKTA OSS</h3>
  <div class="contact" style="top:107px">
    <svg width="30" height="30" viewBox="0 0 24 24" fill="none" stroke="#fff" stroke-width="1.6"><path d="M5 3h4l2 5-2.5 1.5a11 11 0 0 0 6 6L16 13l5 2v4a2 2 0 0 1-2 2A16 16 0 0 1 3 5a2 2 0 0 1 2-2z"/></svg>
    <div><div class="big">010-4400870</div><div class="small">Växeln är öppen vardagar 8-17</div></div>
  </div>
  <div class="contact" style="top:164px">
    <svg width="30" height="22" viewBox="0 0 30 22" fill="none" stroke="#fff" stroke-width="2" style="margin-top:6px"><rect x="1" y="1" width="28" height="20"/><path d="m1 1 14 11L29 1"/></svg>
    <div><div class="big">info@kolrev.se</div><div class="small">Synpunkter om hemsidan skickas till web@kolrev.se</div></div>
  </div>
  <div class="contact" style="top:229px">
    <svg width="28" height="34" viewBox="0 0 24 30" fill="#fff"><path d="M12 0a11 11 0 0 0-11 11c0 8 11 19 11 19s11-11 11-19A11 11 0 0 0 12 0zm0 16a5 5 0 1 1 0-10 5 5 0 0 1 0 10z"/></svg>
    <div><div class="big">Kolrev Sverige AB</div><div class="small">Ekbacken 12<br>241 30 Ljungdal</div></div>
  </div>

  <h3 class="fcol-title" style="left:916px">FÖLJ OSS HÄR</h3>
  <a class="social" style="top:107px" href="#"><i></i>FOTOBOK</a>
  <a class="social" style="top:160px" href="#"><i></i>KVITTER</a>
  <a class="social" style="top:213px" href="#"><i></i>BILDFLÖDE</a>
  <a class="social" style="top:266px" href="#"><i></i>FILMKANAL</a>

  <p class="copy">© 2018 Kolrev Sverige AB. All Rights Reserved.</p>
</footer>

</body>
</html>
```